Velmira sailing boat for love and romance seekers*

We will pay extra 200$ for the winning design! So, we have a sailing boat, Harlow 58 KT called Velmira, which we’d like to give for charter in Turkey and maybe other countries. Need a dedicated web page, with gallery, calendar, videos, customer reviews, possibility to pay down payment, legal disclosures and in 3 languages (English, Russian and Turkish). Also, there should be info on toys and crew. We can also agree on a monthly fee for maintenance and updates. It’s really important to show the details, so that potential customers can see clearly that the boat is in perfect shape. If needed, we can even make a 3D of the interior, or any other materials that you might need. People should also have the possibility to see the sailing routes that they can chose and experience while cruising. Additionally, we can organize diving tours, surfing lessons, and any other activities.

Target Market(s)

Family with kids. Those people that are looking for more luxury than what’s usually offered with other boats. This is a middle segment between usual boats and super luxury boats. Also, it’s for those people that want romance, love and are looking for Unforgetable experiences with their family.

Coding

Coded - Design and coding required

Number of Pages Required

3 page

Font styles to use
Sans Serif

Requirements
Must have
• Boat has lots of options, and we have a tender boat with which one can waterski, pull ringos and other toys. It’s big enough to carry all guests at the same time and comfortable to reach safely any remote beach location. We have brand new snorkeling and diving equipment, new paddle and surfing boards, new dartino, Gorvetto and life jackets for all age groups. Also, we should have a page on crew, who they are and whom additionally they can chose (for example cook or cleaning staff).
Nice to have
• We’d like to see a page with will make you dream, feel romantic and in love. To ensure the visitors that our boat is perfect for a dream holiday. Imagine being in a secluded white sand beach bay all alone with your loved ones, in a beautiful luxurious boat. Now stop dreaming and join us to make your dreams come true. Lastly, because of virus, we should also mention that we do proper cleaning of boat after every use (COVID free).

Vēlmirā is a Sanskrit word that means "wandering" or "world", with the connotation of cyclic, circuitous change. It is also the concept of rebirth and "cyclicality of all life, matter, existence", a fundamental belief of most Indian religions. In short, it is the cycle of death and rebirth.
Should not have
• It should not be only for one system, all devices should be able to see that page properly.

```html
<!DOCTYPE html>
<html lang="en">
<head>
<meta charset="utf-8">
<title>Velmira – Family Sailing Boat</title>
<link href="https://fonts.googleapis.com/css2?family=Nunito:wght@400;600;700;800;900&family=Nunito+Sans:wght@300;400;600;700&display=swap" rel="stylesheet">
<style>
:root{
  --green-dark:#0b5944;
  --green-deep:#08402f;
  --teal:#14e3b5;
  --teal-soft:#8ef0e6;
  --cyan-light:#e5fbfd;
  --orange:#ff9b17;
  --text:#4b5a57;
  --muted:#8a9896;
  --white:#ffffff;
  --line:#d9e2e0;
}
*{box-sizing:border-box;margin:0;padding:0}
html,body{width:1200px;height:5347px;overflow:hidden}
body{position:relative;background:var(--white);font-family:"Nunito Sans",sans-serif;color:var(--text)}
.abs{position:absolute}
h1,h2,h3{font-family:"Nunito",sans-serif;color:var(--green-dark)}

/* header */
.site-header{position:absolute;left:0;top:0;width:1200px;height:80px;background:var(--white);box-shadow:0 2px 8px rgba(0,0,0,.06);z-index:5}
.brand{position:absolute;left:100px;top:18px;font-family:"Nunito",sans-serif;font-size:30px;font-weight:700;color:var(--green-dark);line-height:1}
.brand-tag{position:absolute;left:108px;top:58px;font-size:9px;letter-spacing:1.5px;color:var(--green-dark);font-weight:700}
.topbar{position:absolute;right:100px;top:8px;display:flex;gap:14px;align-items:center;font-size:11px;color:var(--muted)}
.topbar .dot{width:11px;height:11px;border-radius:50%;background:#8a9896;display:inline-block}
.nav{position:absolute;left:545px;top:45px;display:flex;gap:48px;font-size:14px;font-weight:700;color:var(--green-dark);letter-spacing:.3px}
.btn-charter{position:absolute;left:945px;top:37px;width:157px;height:36px;background:var(--orange);color:var(--white);font-weight:800;font-size:13px;display:flex;align-items:center;justify-content:center;border-radius:3px;letter-spacing:.3px}

/* hero */
.hero-photo{left:0;top:80px;width:1200px;height:626px;background:
  radial-gradient(ellipse 260px 200px at 700px 210px,rgba(255,236,214,.75),transparent 70%),
  radial-gradient(ellipse 240px 260px at 920px 330px,rgba(245,250,255,.8),transparent 70%),
  radial-gradient(ellipse 200px 160px at 500px 300px,rgba(30,60,110,.45),transparent 70%),
  radial-gradient(ellipse 160px 120px at 780px 160px,rgba(220,40,70,.35),transparent 70%),
  linear-gradient(180deg,#d6eefa 0%,#a7d6ee 20%,#7fbad9 34%,#5f8fa8 37%,#3f86b8 45%,#2f74a8 70%,#5aa2cc 90%,#cfe6f1 100%)}
.hero-card{left:110px;top:353px;width:747px;height:191px;background:rgba(255,255,255,.82)}
.play{position:absolute;width:56px;height:56px;border-radius:50%;background:var(--white);box-shadow:0 3px 12px rgba(0,0,0,.15)}
.play::after{content:"";position:absolute;left:22px;top:18px;border-left:16px solid var(--teal);border-top:10px solid transparent;border-bottom:10px solid transparent}
.hero-card .play{left:38px;top:68px}
.hero-kicker{position:absolute;left:140px;top:22px;font-size:17px;color:var(--text)}
.hero-title{position:absolute;left:140px;top:46px;font-size:42px;line-height:45px;font-weight:800;color:var(--green-dark)}
.hero-sub{position:absolute;left:140px;top:148px;font-size:17px;color:var(--text)}

.feature{width:457px;height:184px;box-shadow:0 10px 25px rgba(0,0,0,.1);overflow:hidden}
.feature .photo{position:absolute;inset:0}
.feature span{position:absolute;left:38px;top:58px;font-family:"Nunito",sans-serif;font-size:26px;line-height:33px;font-weight:600;color:var(--green-dark)}
.ph-family{background:
  radial-gradient(ellipse 90px 80px at 340px 110px,rgba(40,60,100,.55),transparent 70%),
  radial-gradient(ellipse 80px 70px at 260px 120px,rgba(220,190,160,.8),transparent 70%),
  linear-gradient(90deg,#f4f8fa 0%,#eef4f7 35%,#b9d4e2 60%,#7aa9c4 100%)}
.ph-lounge{background:
  radial-gradient(ellipse 120px 60px at 300px 150px,rgba(160,110,70,.6),transparent 70%),
  radial-gradient(ellipse 110px 70px at 380px 60px,rgba(255,255,255,.9),transparent 70%),
  linear-gradient(90deg,#f6f7f8 0%,#eef0f1 35%,#d8d0c6 60%,#b79a80 100%)}
.ph-friends{background:
  radial-gradient(ellipse 110px 60px at 260px 110px,rgba(80,140,190,.6),transparent 70%),
  radial-gradient(ellipse 60px 80px at 400px 60px,rgba(120,200,90,.55),transparent 70%),
  linear-gradient(90deg,#f4f8fa 0%,#e7f1f6 35%,#a7cde2 60%,#3f8fc0 100%)}
.ph-couple{background:
  radial-gradient(ellipse 100px 90px at 300px 90px,rgba(200,140,110,.55),transparent 70%),
  radial-gradient(ellipse 90px 70px at 380px 140px,rgba(200,90,130,.45),transparent 70%),
  linear-gradient(90deg,#f8f8f8 0%,#f3efe9 35%,#e6d5c4 60%,#a9c9d8 100%)}

/* water games */
.section-title{font-size:60px;font-weight:800;text-align:center;width:1200px;left:0}
.game{height:353px;top:1328px}
.game-active{left:421px;top:1297px;width:354px;height:411px;box-shadow:0 14px 30px rgba(0,0,0,.2);background:
  radial-gradient(ellipse 60px 40px at 200px 340px,rgba(40,90,150,.7),transparent 70%),
  radial-gradient(ellipse 140px 60px at 180px 130px,rgba(60,110,110,.6),transparent 70%),
  linear-gradient(180deg,#8bc4c9 0%,#6fb0b8 25%,#3f7e86 38%,#3f8c95 55%,#6aa9ae 80%,#2b6f7a 100%)}
.game-active .label{position:absolute;width:100%;top:185px;text-align:center;color:var(--white);font-family:"Nunito",sans-serif;font-weight:800;font-size:36px;letter-spacing:1px}
.ribbon{position:absolute;left:32px;top:0;width:50px;height:62px;background:var(--teal);clip-path:polygon(0 0,100% 0,100% 100%,50% 75%,0 100%)}
.g-dive{background:radial-gradient(ellipse 30px 90px at 50px 220px,rgba(10,30,60,.8),transparent 70%),linear-gradient(180deg,#3a86c0,#154c80 60%,#0d3d6b)}
.g-ringo{background:
  radial-gradient(ellipse 150px 60px at 150px 190px,rgba(30,40,130,.85),transparent 70%),
  radial-gradient(ellipse 90px 60px at 210px 110px,rgba(220,170,140,.7),transparent 70%),
  radial-gradient(ellipse 120px 80px at 80px 300px,rgba(255,255,255,.8),transparent 70%),
  linear-gradient(160deg,#3e6f9e,#8fb0cc 45%,#d7e3ee 60%,#47628d)}
.g-snork{background:
  radial-gradient(ellipse 90px 40px at 190px 180px,rgba(255,140,30,.75),transparent 70%),
  radial-gradient(ellipse 80px 30px at 100px 260px,rgba(190,230,60,.6),transparent 70%),
  linear-gradient(160deg,#3fd3d0,#12a5b5 55%,#5fd8d2)}
.g-surf{background:radial-gradient(ellipse 40px 60px at 60px 260px,rgba(255,120,70,.7),transparent 70%),linear-gradient(160deg,#2f6f9c,#4a8db8 40%,#dfeef5)}
.tabs{left:0;top:1796px;width:1200px;height:50px;font-size:18px}
.tabs span{position:absolute;top:12px;color:#5f6f6c}
.tab-pill{position:absolute;left:523px;top:0;width:154px;height:48px;border:2px solid var(--teal);border-radius:24px;background:var(--white)}
.tab-pill::before{content:"";position:absolute;left:68px;top:-10px;border-bottom:9px solid var(--teal);border-left:8px solid transparent;border-right:8px solid transparent}

/* romance */
.romance-photo{left:0;top:1960px;width:1200px;height:631px;background:
  radial-gradient(ellipse 180px 240px at 830px 300px,rgba(238,196,178,.95),transparent 70%),
  radial-gradient(ellipse 120px 140px at 720px 220px,rgba(245,235,225,.85),transparent 70%),
  radial-gradient(ellipse 330px 120px at 960px 600px,rgba(150,110,80,.85),transparent 70%),
  linear-gradient(180deg,#c4dbe6 0%,#a9c9da 18%,#7ea6bc 22%,#4f7b95 45%,#3b6680 75%,#2f5670 100%)}
.romance-title{left:110px;top:2112px;font-size:31px;line-height:38px;font-weight:800;color:var(--green-dark)}
.romance-text{left:110px;top:2212px;width:420px;font-size:15px;line-height:31px;color:#33423f}
.romance-photo-play{left:108px;top:2342px;width:62px;height:62px;border-radius:50%;background:rgba(255,255,255,.3)}
.romance-photo-play::after{content:"";position:absolute;left:25px;top:20px;border-left:17px solid rgba(255,255,255,.85);border-top:11px solid transparent;border-bottom:11px solid transparent}

/* crew */
.crew-title{left:110px;top:2738px;font-size:60px;line-height:63px;font-weight:900;color:var(--green-dark)}
.crew-text{left:110px;top:3072px;width:380px;font-size:14px;line-height:31px;color:#3f4d4a}
.crew-text u{color:var(--green-dark)}
.crew-photo{left:498px;top:2747px;width:702px;height:498px;background:
  radial-gradient(ellipse 110px 80px at 620px 370px,rgba(250,210,20,.9),transparent 70%),
  radial-gradient(ellipse 90px 90px at 170px 320px,rgba(250,210,20,.9),transparent 70%),
  radial-gradient(ellipse 120px 60px at 200px 420px,rgba(70,180,210,.8),transparent 70%),
  radial-gradient(ellipse 220px 150px at 470px 330px,rgba(200,200,205,.8),transparent 70%),
  radial-gradient(ellipse 130px 150px at 460px 160px,rgba(210,160,130,.7),transparent 70%),
  linear-gradient(135deg,#d8d2c6 0%,#b8ae9e 40%,#cfc8bc 70%,#5f5a55 100%)}
.crew-active{left:100px;top:3143px;width:398px;height:50px;background:var(--teal);color:var(--green-dark);font-weight:800;font-size:20px;padding:12px 0 0 26px;font-family:"Nunito",sans-serif}
.crew-next{left:126px;top:3208px;font-size:20px;color:var(--green-dark);font-family:"Nunito",sans-serif}

/* reviews */
.review-photo{left:112px;top:3571px;width:488px;height:284px;background:
  radial-gradient(ellipse 110px 70px at 280px 170px,rgba(30,60,110,.5),transparent 70%),
  radial-gradient(ellipse 50px 40px at 320px 70px,rgba(220,40,70,.45),transparent 70%),
  radial-gradient(ellipse 140px 60px at 300px 250px,rgba(250,250,250,.85),transparent 70%),
  linear-gradient(180deg,#d6eefa 0%,#a7d6ee 25%,#5f8fa8 32%,#3f86b8 50%,#6fb3d6 80%,#e7f2f6 100%)}
.review-name{left:635px;top:3600px;font-size:32px;font-weight:600;font-family:"Nunito",sans-serif;color:var(--green-dark)}
.stars{left:635px;top:3648px;display:flex;gap:9px}
.stars svg{width:17px;height:17px}
.review-text{left:633px;top:3688px;width:420px;font-size:15px;line-height:31px;color:#3f4d4a}
.review-more{left:633px;top:3812px;font-size:15px;color:var(--green-dark);text-decoration:underline}
.quote{left:988px;top:3598px;font-family:"Nunito",sans-serif;font-size:90px;font-weight:900;color:#dfe6e5;line-height:1}
.dots{left:455px;top:3930px;display:flex;align-items:center;gap:18px}
.dots i{display:block;width:12px;height:12px;border-radius:50%;border:1.5px solid var(--teal)}
.dots i.on{background:var(--teal)}
.dots b{display:block;width:24px;height:24px;border-radius:50%;position:relative}

/* booking */
.date-title{left:116px;top:4108px;font-size:60px;font-weight:800;color:var(--green-dark)}
.form-card{left:112px;top:4256px;width:475px;height:540px;background:var(--white);box-shadow:0 8px 30px rgba(0,0,0,.1);border-radius:4px}
.field{position:absolute;height:34px;border-bottom:1.5px solid var(--line);font-size:12px;color:#98a4a2;padding-top:10px;padding-left:28px}
.field::before{content:"";position:absolute;left:4px;top:11px;width:12px;height:12px;border:1.5px solid #b6c0be;border-radius:3px}
.field.select::after{content:"";position:absolute;right:10px;top:13px;width:7px;height:7px;border-right:1.5px solid #98a4a2;border-bottom:1.5px solid #98a4a2;transform:rotate(45deg)}
.form-btn{position:absolute;left:68px;top:470px;width:330px;height:46px;background:var(--orange);color:var(--white);font-weight:800;font-size:15px;display:flex;align-items:center;justify-content:center;border-radius:3px}
.card-shapes{position:absolute;left:310px;top:401px;display:flex;gap:6px;align-items:center}
.card-shapes i{display:block;width:32px;height:20px;background:#dfe4e3;border-radius:3px}

.cal-head{left:656px;top:4258px;width:417px;height:36px;background:var(--teal);color:var(--green-dark);font-size:20px;text-align:center;padding-top:5px}
.cal-head svg{position:absolute;top:9px;width:18px;height:18px}
.cal{left:0;top:0}
.cal span{position:absolute;width:50px;text-align:center;font-size:21px;color:var(--green-dark);transform:translateX(-25px)}
.cal span.dow{font-size:13px;font-style:italic;color:#7c8a88}
.cal-range{left:703px;top:4440px;width:250px;height:54px;border-radius:27px;background:var(--teal)}

/* footer */
.site-footer{left:0;top:4953px;width:1200px;height:394px;background:linear-gradient(180deg,#11a37d 0%,#0c6c52 35%,#0a4a39 100%)}
.site-footer .f-brand{position:absolute;left:116px;top:72px;font-family:"Nunito",sans-serif;font-size:32px;font-weight:700;color:var(--white)}
.f-addr{position:absolute;left:116px;top:146px;font-size:15px;line-height:27px;color:var(--white)}
.f-social{position:absolute;left:116px;top:240px;display:flex;gap:14px}
.f-social i{display:block;width:20px;height:20px;border-radius:50%;background:var(--white)}
.f-copy{position:absolute;left:116px;top:285px;font-size:11px;color:var(--white)}
.f-col{position:absolute;top:104px;font-size:15px;line-height:35px;color:var(--white)}
</style>
</head>
<body>

<header class="site-header">
  <div class="brand">Velmira</div>
  <div class="brand-tag">- FAMILY SAILING BOAT -</div>
  <div class="topbar">
    <span>&#9742; CALL US (+90) 4417 2083</span>
    <span style="display:flex;gap:8px"><i class="dot"></i><i class="dot"></i><i class="dot"></i><i class="dot"></i></span>
    <span>EN &#9662;</span>
  </div>
  <nav class="nav"><span>ABOUT US</span><span>GAMES</span><span>EVENTS</span><span>CREW</span></nav>
  <div class="btn-charter">CHARTER NOW!</div>
</header>

<!-- hero -->
<div class="abs hero-photo" role="img" aria-label="Family of four relaxing on the deck of a sailing yacht over blue sea"></div>
<svg class="abs" style="left:0;top:640px" width="1200" height="500" viewBox="0 0 1200 500">
  <path d="M1000 210 C1080 170 1200 180 1200 180 L1200 420 C1150 420 1080 410 1040 380 Z" fill="var(--teal-soft)"/>
  <path d="M650 300 C800 420 1000 470 1200 480" fill="none" stroke="var(--teal-soft)" stroke-width="2"/>
</svg>
<div class="abs hero-card">
  <div class="play"></div>
  <div class="hero-kicker">Turkey's Family Yacht</div>
  <div class="hero-title">Imagine being in a scheduled<br>white sand beach bay</div>
  <div class="hero-sub">All alone with your loved ones, in a beautiful luxurious boat.</div>
</div>

<div class="abs feature" style="left:118px;top:619px"><div class="photo ph-family" role="img" aria-label="Family sitting together on a yacht bow"></div><span>Pleasure<br>with family</span></div>
<div class="abs feature" style="left:623px;top:619px"><div class="photo ph-lounge" role="img" aria-label="Luxurious yacht interior lounge"></div><span>Enjoy your moment<br>with the luxurious service</span></div>
<div class="abs feature" style="left:118px;top:847px"><div class="photo ph-friends" role="img" aria-label="Friends posing on a sailing boat deck"></div><span>Unforgetable<br>experiences</span></div>
<div class="abs feature" style="left:623px;top:847px"><div class="photo ph-couple" role="img" aria-label="Couple embracing by the sea"></div><span>Full of love and<br>happiness</span></div>

<!-- water games -->
<h2 class="abs section-title" style="top:1168px">More Fun with Water Games</h2>
<svg class="abs" style="left:0;top:1660px" width="340" height="170" viewBox="0 0 340 170"><path d="M0 20 L300 20 C340 60 330 130 250 150 C170 170 60 175 0 150 Z" fill="var(--teal)"/></svg>
<div class="abs game g-dive" style="left:0;width:83px" role="img" aria-label="Diver under water"></div>
<div class="abs game g-ringo" style="left:102px;width:307px" role="img" aria-label="People riding an inflatable ringo"></div>
<div class="abs game-active" role="img" aria-label="Waterskier on a lake with mountains"><div class="ribbon"></div><div class="label">WATERSKI</div></div>
<div class="abs game g-snork" style="left:787px;width:307px" role="img" aria-label="Snorkeler swimming in turquoise water"></div>
<div class="abs game g-surf" style="left:1113px;width:87px" role="img" aria-label="Surfer on a wave"></div>

<div class="abs tabs">
  <div class="tab-pill"></div>
  <span style="left:172px">Snorkeling</span>
  <span style="left:300px">Diving</span>
  <span style="left:395px">Pull Ringos</span>
  <span style="left:563px">Waterski</span>
  <span style="left:711px">Paddle &amp; Surfing</span>
  <span style="left:900px">Dartino</span>
  <span style="left:996px">Other games</span>
</div>

<!-- romance -->
<div class="abs romance-photo" role="img" aria-label="Couple embracing on a yacht deck at sunset over the sea"></div>
<h2 class="abs romance-title">Romantic Moments with<br>One of Person You Loved</h2>
<p class="abs romance-text">Pellentesque at tincidunt lorem, sollicitudin eleifend ante. Nunc vestibulum facilisis leo. Mauris iaculis suscipit ligula, nec luctus ligula pulvinar in.</p>
<div class="abs romance-photo-play"></div>

<!-- crew + reviews background -->
<svg class="abs" style="left:0;top:2834px" width="1200" height="1160" viewBox="0 0 1200 1160">
  <path d="M0 0 L1200 0 L1200 1070 C900 1120 400 1160 0 1150 Z" fill="var(--cyan-light)"/>
  <circle cx="16" cy="400" r="16" fill="var(--teal)"/>
  <path d="M0 430 C30 500 90 500 115 470" fill="none" stroke="var(--teal)" stroke-width="20" stroke-linecap="round"/>
  <path d="M0 640 C60 670 100 640 115 620" fill="none" stroke="var(--teal)" stroke-width="20" stroke-linecap="round"/>
</svg>
<div class="abs" style="left:0;top:2747px;width:498px;height:87px;background:var(--white)"></div>

<h2 class="abs crew-title">You Can<br>Choose<br>Your<br>Additional<br>Crew</h2>
<p class="abs crew-text">We provide additional crew in order to you focus on your dream pleasure. <u>view our crew</u></p>
<div class="abs crew-photo" role="img" aria-label="Smiling crew member wiping a table with a blue cloth and yellow gloves"></div>
<div class="abs crew-active">Cleaning Staff &gt;</div>
<div class="abs crew-next">Cooking Staff &gt;</div>

<h2 class="abs section-title" style="top:3400px">What They Say..</h2>
<div class="abs review-photo" role="img" aria-label="Family relaxing on a sailing yacht deck"></div>
<div class="abs review-name">Daniel Arkwright</div>
<div class="abs stars">
  <svg viewBox="0 0 20 20"><path d="M10 1l2.6 6 6.4.5-4.9 4.2 1.5 6.3L10 14.6 4.4 18l1.5-6.3L1 7.5 7.4 7z" fill="var(--orange)"/></svg>
  <svg viewBox="0 0 20 20"><path d="M10 1l2.6 6 6.4.5-4.9 4.2 1.5 6.3L10 14.6 4.4 18l1.5-6.3L1 7.5 7.4 7z" fill="var(--orange)"/></svg>
  <svg viewBox="0 0 20 20"><path d="M10 1l2.6 6 6.4.5-4.9 4.2 1.5 6.3L10 14.6 4.4 18l1.5-6.3L1 7.5 7.4 7z" fill="var(--orange)"/></svg>
  <svg viewBox="0 0 20 20"><path d="M10 1l2.6 6 6.4.5-4.9 4.2 1.5 6.3L10 14.6 4.4 18l1.5-6.3L1 7.5 7.4 7z" fill="var(--orange)"/></svg>
  <svg viewBox="0 0 20 20"><path d="M10 1l2.6 6 6.4.5-4.9 4.2 1.5 6.3L10 14.6 4.4 18l1.5-6.3L1 7.5 7.4 7z" fill="var(--orange)"/></svg>
</div>
<div class="abs quote">&rdquo;</div>
<p class="abs review-text">Pellentesque at tincidunt lorem, sollicitudin eleifend ante. Nunc vestibulum facilisis leo. Mauris iaculis suscipit ligula, nec luctus ligula pulvinar in.</p>
<div class="abs review-more">more reviews &gt;</div>
<div class="abs dots">
  <b style="background:#bff3e7"><svg width="24" height="24" viewBox="0 0 24 24"><path d="M14 7l-5 5 5 5" fill="none" stroke="var(--white)" stroke-width="2.5"/></svg></b>
  <i class="on"></i><i></i><i></i><i></i><i></i>
  <b style="background:var(--teal)"><svg width="24" height="24" viewBox="0 0 24 24"><path d="M10 7l5 5-5 5" fill="none" stroke="var(--white)" stroke-width="2.5"/></svg></b>
</div>

<!-- booking -->
<h2 class="abs date-title">Lets Pick Your Date</h2>
<svg class="abs" style="left:0;top:4560px" width="1200" height="400" viewBox="0 0 1200 400">
  <path d="M80 360 C40 250 120 150 220 170 C330 190 450 250 460 330 C465 380 430 393 400 393 L90 393 Z" fill="var(--teal-soft)"/>
  <path d="M0 260 C250 120 520 80 700 392" fill="none" stroke="var(--teal-soft)" stroke-width="2"/>
</svg>
<div class="abs form-card">
  <div class="field" style="left:68px;top:36px;width:330px">Istanbul, Turkey</div>
  <div class="field" style="left:68px;top:100px;width:155px">Date in</div>
  <div class="field" style="left:243px;top:100px;width:155px">10:00 a.m</div>
  <div class="field" style="left:68px;top:166px;width:155px">Date Out</div>
  <div class="field" style="left:243px;top:166px;width:155px">12:00 p.m</div>
  <div class="field select" style="left:68px;top:226px;width:330px">Boat Type</div>
  <div class="field select" style="left:68px;top:298px;width:330px">Additional Crew</div>
  <div class="field select" style="left:68px;top:376px;width:220px">Payment Method</div>
  <div class="card-shapes"><i></i><i></i></div>
  <div class="form-btn">CHARTER NOW!</div>
</div>

<div class="abs cal-head">August, 2020
  <svg style="left:10px" viewBox="0 0 18 18"><path d="M11 3L5 9l6 6" fill="none" stroke="var(--green-dark)" stroke-width="2"/></svg>
  <svg style="right:10px" viewBox="0 0 18 18"><path d="M7 3l6 6-6 6" fill="none" stroke="var(--green-dark)" stroke-width="2"/></svg>
</div>
<div class="abs cal-range"></div>
<div class="abs cal">
  <span class="dow" style="left:664px;top:4330px">S</span><span class="dow" style="left:727px;top:4330px">M</span><span class="dow" style="left:791px;top:4330px">T</span><span class="dow" style="left:853px;top:4330px">W</span><span class="dow" style="left:916px;top:4330px">T</span><span class="dow" style="left:980px;top:4330px">F</span><span class="dow" style="left:1042px;top:4330px">S</span>
  <span style="left:980px;top:4382px">1</span><span style="left:1042px;top:4382px">2</span>
  <span style="left:664px;top:4444px">3</span><span style="left:733px;top:4444px">4</span><span style="left:795px;top:4444px">5</span><span style="left:858px;top:4444px">6</span><span style="left:922px;top:4444px">7</span><span style="left:980px;top:4444px">8</span><span style="left:1042px;top:4444px">9</span>
  <span style="left:664px;top:4505px">10</span><span style="left:727px;top:4505px">11</span><span style="left:791px;top:4505px">12</span><span style="left:853px;top:4505px">13</span><span style="left:916px;top:4505px">14</span><span style="left:980px;top:4505px">15</span><span style="left:1042px;top:4505px">16</span>
  <span style="left:664px;top:4567px">17</span><span style="left:727px;top:4567px">18</span><span style="left:791px;top:4567px">19</span><span style="left:853px;top:4567px">20</span><span style="left:916px;top:4567px">21</span><span style="left:980px;top:4567px">22</span><span style="left:1042px;top:4567px">23</span>
  <span style="left:664px;top:4627px">24</span><span style="left:727px;top:4627px">25</span><span style="left:791px;top:4627px">26</span><span style="left:853px;top:4627px">27</span><span style="left:916px;top:4627px">28</span><span style="left:980px;top:4627px">29</span><span style="left:1042px;top:4627px">30</span>
  <span style="left:1042px;top:4689px">31</span>
</div>

<!-- footer -->
<footer class="abs site-footer">
  <div class="f-brand">Velmira</div>
  <div class="f-addr">Kordon Sokak 14,<br>Bodrum, Türkiye<br>081-555-204-316</div>
  <div class="f-social"><i></i><i></i><i></i><i></i></div>
  <div class="f-copy">&copy; 2020. Velmira Alright Reserve</div>
  <div class="f-col" style="left:604px">Facilities<br>Toys<br>Events<br>Crew<br>Inquiry</div>
  <div class="f-col" style="left:762px">Snorkeling<br>Diving<br>Surfing<br>Dartino</div>
  <div class="f-col" style="left:915px">Blog<br>Newsletter</div>
</footer>

</body>
</html>
```